Asia based real estate financing firm needs and AWESOME design for a biz card -Harbor Lending Circle

Looking for a stylish, & corporate-looking business card for a real estate financing brokerage firm in Asia, offering global mortgage loans. I uploaded our current logos. We would like to add a splash of color (perhaps the house icon) or any other suggestions are open. For the winning designer, we have a lot of work! Thanks and best of luck!

Target Market(s)

Real estate investors globally. We want to look more like a BANK and NOT a real estate company. Please don't play up on a "house" design.

Industry/Entity Type

Banking

Contact Information for Business Card

Harbor Lending Circle
Peter Wilks
Co-Founder | Partner

14 Cassia Lane, Suite 310
Singapore 047219
www.hlc-example.asia
peterwilks@hlc-example.asia
+65 555-0142
WeChat: peterwilks

Colors

Designer to choose colors to be used in the design.

Requirements
Must have
• Must have the standard business requirements for a card; name, address, email, etc
• Can be horizontal or vertical.
Nice to have
• It would be great to see some sort of variation to the logo with a pop of color. Red is good as we're in Asia, however, other options work as well.
• Our tag line is - Borderless mortgages. It doesn't have to be on the card but might be nice.
• I'd like to start seeing our tagline within the cards as well. - Borderless mortgages.
• Also, please add our location. The location for this card is Singapore so perhaps it can be highlighted or emphasised in some way.
• Singapore | Hong Kong | Shanghai | Manila
• As we will soon open an office in Shanghai, having an option for both languages would be great.
Should not have
• I'm exceited and open to your creativity ... knock it out of the park!

```html
<!DOCTYPE html>
<html lang="en">
<head>
<meta charset="utf-8">
<title>Harbor Lending Circle – Business Card</title>
<link rel="stylesheet" href="https://fonts.googleapis.com/css2?family=Marcellus&family=Questrial&display=swap">
<style>
  :root {
    --stage: #e7e5e1;
    --card-black: #0b0b0b;
    --band-grey: #b9b9b9;
    --accent-yellow: #f5ee0c;
    --name-gold: #e9b825;
    --text-white: #f4f4f4;
    --contact-gold: #e7b52a;
  }
  * { box-sizing: border-box; margin: 0; padding: 0; }
  html, body {
    width: 1200px; height: 900px; overflow: hidden;
    background: var(--stage);
  }
  .stage { position: relative; width: 1200px; height: 900px; }

  .card {
    position: absolute; left: 250px;
    width: 700px; height: 400px;
    background: var(--card-black);
    overflow: hidden;
    box-shadow: 0 6px 18px rgba(0,0,0,0.18);
  }
  .card--back { top: 30px; }
  .card--front { top: 470px; }

  .band { position: absolute; left: 0; width: 100%; background: var(--band-grey); }
  .band--top { top: 0; height: 12px; }
  .band--bottom { bottom: 0; height: 16px; }

  .wordmark {
    font-family: "Marcellus", serif;
    color: var(--text-white);
    text-transform: uppercase;
    text-align: center;
    letter-spacing: 3px;
    line-height: 1.15;
  }
  .card--back .wordmark {
    position: absolute; left: 0; top: 150px; width: 100%;
    font-size: 40px;
  }
  .card--front .wordmark {
    position: absolute; left: 30px; top: 160px; width: 250px;
    font-size: 28px; letter-spacing: 2px;
  }

  .accents { position: absolute; inset: 0; }

  .divider {
    position: absolute; left: 300px; top: 46px;
    width: 2px; height: 310px; background: var(--accent-yellow);
  }

  .holder { position: absolute; left: 420px; top: 54px; }
  .holder__name {
    font-family: "Marcellus", serif;
    font-size: 36px; font-weight: 400; color: var(--name-gold); line-height: 1;
  }
  .holder__title {
    font-family: "Questrial", sans-serif;
    font-size: 14px; color: var(--text-white); margin-top: 4px;
  }

  .contacts { position: absolute; left: 330px; top: 128px; list-style: none; }
  .contact {
    display: flex; align-items: flex-start; gap: 12px;
    font-family: "Questrial", sans-serif;
    font-size: 16px; color: var(--contact-gold);
    letter-spacing: 0.5px; line-height: 1.2;
    margin-bottom: 12px;
  }
  .contact__icon { flex: 0 0 22px; width: 22px; height: 22px; }
</style>
</head>
<body>
<main class="stage">

  <section class="card card--back" aria-label="Business card, back">
    <div class="band band--top"></div>
    <p class="wordmark">Harbor Lending Circle</p>
    <div class="band band--bottom"></div>
  </section>

  <section class="card card--front" aria-label="Business card, front">
    <svg class="accents" width="700" height="400" viewBox="0 0 700 400" aria-hidden="true">
      <polygon points="0,12 92,12 0,58" fill="var(--accent-yellow)"/>
      <polygon points="112,12 138,12 0,82 0,69" fill="var(--accent-yellow)"/>
      <polygon points="700,384 560,384 700,300" fill="var(--accent-yellow)"/>
      <polygon points="528,384 498,384 700,262 700,279" fill="var(--accent-yellow)"/>
    </svg>
    <div class="band band--top"></div>
    <div class="band band--bottom"></div>

    <p class="wordmark">Harbor Lending Circle</p>
    <div class="divider"></div>

    <div class="holder">
      <h1 class="holder__name">Peter Wilks</h1>
      <p class="holder__title">Co-Founder | Partner</p>
    </div>

    <ul class="contacts">
      <li class="contact">
        <svg class="contact__icon" viewBox="0 0 22 22" aria-hidden="true">
          <circle cx="11" cy="11" r="10" fill="none" stroke="var(--contact-gold)" stroke-width="1.5"/>
          <path d="M6 9 Q11 5 16 9 L14.5 10.5 L13 9 L9 9 L7.5 10.5 Z M7.5 11 H14.5 L15.5 15.5 H6.5 Z" fill="var(--contact-gold)"/>
        </svg>
        <span>+65 555-0142</span>
      </li>
      <li class="contact">
        <svg class="contact__icon" viewBox="0 0 22 22" aria-hidden="true">
          <circle cx="11" cy="11" r="10" fill="none" stroke="var(--contact-gold)" stroke-width="1.5"/>
          <path d="M5 11 L11 5.5 L17 11 H15 V16 H12.5 V13 H9.5 V16 H7 V11 Z" fill="var(--contact-gold)"/>
        </svg>
        <span>14 Cassia Lane, Suite 310<br>Singapore 047219</span>
      </li>
      <li class="contact">
        <svg class="contact__icon" viewBox="0 0 22 22" aria-hidden="true">
          <circle cx="11" cy="11" r="10" fill="none" stroke="var(--contact-gold)" stroke-width="1.5"/>
          <rect x="5.5" y="7.5" width="11" height="7.5" fill="var(--contact-gold)"/>
          <path d="M5.5 7.5 L11 12 L16.5 7.5" fill="none" stroke="var(--card-black)" stroke-width="1"/>
        </svg>
        <span>peterwilks@hlc-example.asia</span>
      </li>
      <li class="contact">
        <svg class="contact__icon" viewBox="0 0 22 22" aria-hidden="true">
          <circle cx="11" cy="11" r="10" fill="none" stroke="var(--contact-gold)" stroke-width="1.5"/>
          <circle cx="11" cy="11" r="5.5" fill="none" stroke="var(--contact-gold)" stroke-width="1.2"/>
          <ellipse cx="11" cy="11" rx="2.3" ry="5.5" fill="none" stroke="var(--contact-gold)" stroke-width="1"/>
          <line x1="5.5" y1="11" x2="16.5" y2="11" stroke="var(--contact-gold)" stroke-width="1"/>
        </svg>
        <span>www.hlc-example.asia</span>
      </li>
      <li class="contact">
        <svg class="contact__icon" viewBox="0 0 22 22" aria-hidden="true">
          <circle cx="11" cy="11" r="10" fill="none" stroke="var(--contact-gold)" stroke-width="1.5"/>
        </svg>
        <span>peterwilks</span>
      </li>
    </ul>
  </section>

</main>
</body>
</html>
```